Digital Marketing Website Design

I need the homepage designed for my new digital marketing agency I am starting. The main goal for this homepage is to drive people to make an appointment for me to discuss their upcoming projects. Here are some examples of the layouts that I would like to emulate.
https://www.tallmarsh.com/
https://www.quillforge.com/
https://pebblenook.com/
https://drvenholt.com/
https://www.quietlyrooted.org/
My main focus is to attract leads that need help with running digital ads such as Chatterly ads and Finder Promos. I do offer other services like SEO and other things but the main focus is digital Ads.
The final design should communicate Orchid Digital is a Digital marketing strategist building predictable revenue for small businesses through digital ads, email and marketing automation.
Target Market(s)
30-55, business owners, income 100K+, ecommerce companies, etc.
Industry/Entity Type
Digital Marketing
Number of Pages Required
2 page
Font styles to use
Requirements
Must have
- An appealing look and feel set to drive people to make an appointment.
Logo
There needs to be a call to action button in the far right of the navigation
The same call to action in the navigation needs to be in each section on the homepage.
I need the homepage and an about us page.

```html
<!DOCTYPE html>
<html lang="en">
<head>
<meta charset="UTF-8">
<title>Orchid Digital – Testimonials</title>
<link rel="stylesheet" href="https://fonts.googleapis.com/css2?family=Raleway:wght@400;500&display=swap">
<style>
  :root {
    --page-bg: #ffffff;
    --band-bg: #f2f1fd;
    --heading: #222222;
    --body-text: #7a7a7a;
    --name-text: #2b2b2b;
    --accent-pink: #ff4fa0;
    --accent-purple: #a64ee0;
    --avatar-fill: #c8c8c8;
    --card-shadow: rgba(0, 0, 0, 0.08);
  }
  * { box-sizing: border-box; margin: 0; padding: 0; }
  html, body {
    width: 1200px;
    height: 540px;
    overflow: hidden;
    background: var(--page-bg);
    font-family: "Raleway", sans-serif;
  }
  .testimonials {
    position: relative;
    width: 1200px;
    height: 540px;
  }
  .testimonials__title {
    position: absolute;
    top: 66px;
    left: 0;
    width: 100%;
    text-align: center;
    font-size: 25px;
    font-weight: 400;
    letter-spacing: 1.5px;
    color: var(--heading);
  }
  .testimonials__list {
    position: absolute;
    top: 144px;
    left: 113px;
    display: flex;
    gap: 26px;
  }
  .quote-card {
    width: 307px;
    height: 271px;
    background: var(--page-bg);
    border-radius: 16px;
    box-shadow: 0 8px 34px var(--card-shadow);
    padding: 30px 22px 0 22px;
  }
  .quote-card__icon {
    display: block;
    width: 30px;
    height: 30px;
    margin: 0 auto;
  }
  .quote-card__text {
    margin-top: 20px;
    height: 92px;
    font-size: 13.5px;
    line-height: 23px;
    letter-spacing: 0.3px;
    color: var(--body-text);
  }
  .quote-card__author {
    margin-top: 26px;
    display: flex;
    align-items: center;
  }
  .quote-card__avatar {
    width: 53px;
    height: 53px;
    border-radius: 50%;
    background: var(--avatar-fill);
    flex-shrink: 0;
  }
  .quote-card__meta { margin-left: 26px; }
  .quote-card__name {
    font-size: 15px;
    font-weight: 500;
    color: var(--name-text);
    line-height: 20px;
  }
  .quote-card__role {
    margin-top: 3px;
    font-size: 13px;
    color: var(--accent-pink);
    line-height: 18px;
  }
  .next-band {
    position: absolute;
    left: 0;
    top: 512px;
    width: 100%;
    height: 28px;
    background: var(--band-bg);
  }
</style>
</head>
<body>
<section class="testimonials">
  <h2 class="testimonials__title">What do they say?</h2>

  <svg width="0" height="0" style="position:absolute">
    <defs>
      <linearGradient id="quoteGradient" x1="0" y1="0" x2="1" y2="1">
        <stop offset="0" stop-color="#ff4fa0"/>
        <stop offset="1" stop-color="#8a4fe6"/>
      </linearGradient>
      <symbol id="quoteIcon" viewBox="0 0 32 32">
        <path d="M9 8 H23 A8 8 0 0 1 23 24 H20 L18 29 L16 24 H9 A8 8 0 0 1 9 8 Z" fill="none" stroke="url(#quoteGradient)" stroke-width="1.4" stroke-linejoin="round"/>
        <path d="M7 3 q-2 1 -2 4 h2.5 v-2.5 h-1.5 q0 -1 1 -1.5z M11 3 q-2 1 -2 4 h2.5 v-2.5 h-1.5 q0 -1 1 -1.5z" fill="url(#quoteGradient)"/>
        <g stroke="url(#quoteGradient)" stroke-width="1.2" stroke-linecap="round">
          <line x1="10" y1="13" x2="22" y2="13"/>
          <line x1="10" y1="16" x2="24" y2="16"/>
          <line x1="10" y1="19" x2="22" y2="19"/>
        </g>
      </symbol>
    </defs>
  </svg>

  <div class="testimonials__list">
    <article class="quote-card">
      <svg class="quote-card__icon" aria-hidden="true"><use href="#quoteIcon"/></svg>
      <p class="quote-card__text">Proin a neque nisi. Nam ipsum nisi, venenatis ut nulla quis, egestas scelerisque orci. Maecenas a finibus odio.</p>
      <div class="quote-card__author">
        <div class="quote-card__avatar" role="img" aria-label="Portrait photo of Clara Benning"></div>
        <div class="quote-card__meta">
          <p class="quote-card__name">Clara Benning</p>
          <p class="quote-card__role">Managing Director</p>
        </div>
      </div>
    </article>

    <article class="quote-card">
      <svg class="quote-card__icon" aria-hidden="true"><use href="#quoteIcon"/></svg>
      <p class="quote-card__text">Integer molestie aliquam gravida. Nullam nec arcu finibus, imperdiet nulla vitae, placerat nibh. Cras maximus venenatis molestie.</p>
      <div class="quote-card__author">
        <div class="quote-card__avatar" role="img" aria-label="Portrait photo of Rowan Ashby"></div>
        <div class="quote-card__meta">
          <p class="quote-card__name">Rowan Ashby</p>
          <p class="quote-card__role">Digital Marketer</p>
        </div>
      </div>
    </article>

    <article class="quote-card">
      <svg class="quote-card__icon" aria-hidden="true"><use href="#quoteIcon"/></svg>
      <p class="quote-card__text">Quisque diam odio, maximus ac consectetur eu, auctor non lorem. Cras quis est non ante ultrices molestie. Ut vehicula et diam at aliquam.</p>
      <div class="quote-card__author">
        <div class="quote-card__avatar" role="img" aria-label="Portrait photo of Elliot Marsh"></div>
        <div class="quote-card__meta">
          <p class="quote-card__name">Elliot Marsh</p>
          <p class="quote-card__role">Website Manager</p>
        </div>
      </div>
    </article>
  </div>

  <div class="next-band"></div>
</section>
</body>
</html>
```